Lena Corvel Business Card

I need a business card that reflects my current website: itslenacorvel.com and screenshot attached. If we keep the color scheme of the site and sample card below that would be ideal. The business card should include the information on the attached sample cards.

Industry/Entity Type

Business

```html
<!DOCTYPE html>
<html lang="en">
<head>
<meta charset="utf-8">
<title>Lena Corvel Business Card</title>
<link rel="stylesheet" href="https://fonts.googleapis.com/css2?family=Raleway:wght@200;300&display=swap">
<style>
  :root {
    --backdrop: #d8d3ce;
    --card-white: #ffffff;
    --teal: #6ac3b1;
    --teal-light: #9dd8cc;
    --teal-pale: #c9ebe4;
    --teal-mist: #eef8f6;
    --ink-white: #ffffff;
  }
  * { margin: 0; padding: 0; box-sizing: border-box; }
  html, body {
    width: 1200px;
    height: 800px;
    overflow: hidden;
    background: var(--backdrop);
    font-family: "Raleway", Arial, sans-serif;
  }
  .canvas {
    width: 1200px;
    height: 800px;
    display: flex;
    align-items: center;
    justify-content: center;
    gap: 60px;
  }
  .card {
    position: relative;
    width: 520px;
    height: 297px;
    overflow: hidden;
    box-shadow: 0 6px 18px rgba(60, 50, 45, 0.18);
  }
  /* Front side */
  .card-front { background: var(--card-white); }
  .card-front .shapes {
    position: absolute;
    inset: 0;
    width: 100%;
    height: 100%;
  }
  .card-front .signature-name {
    position: absolute;
    left: 190px;
    top: 128px;
    font-weight: 300;
    font-size: 40px;
    letter-spacing: 1px;
    color: var(--ink-white);
    white-space: nowrap;
  }
  /* Back side */
  .card-back {
    background: linear-gradient(160deg, var(--teal) 0%, var(--teal-light) 40%, var(--teal-pale) 72%, var(--teal-mist) 100%);
  }
  .card-back .web-address {
    position: absolute;
    left: 34px;
    top: 26px;
    font-weight: 300;
    font-size: 10px;
    letter-spacing: 1px;
    color: var(--ink-white);
    opacity: 0.8;
  }
  .card-back .name {
    position: absolute;
    left: 32px;
    top: 58px;
    font-weight: 200;
    font-size: 52px;
    letter-spacing: 2px;
    color: var(--ink-white);
    white-space: nowrap;
  }
  .card-back .roles {
    position: absolute;
    left: 36px;
    top: 128px;
    font-weight: 300;
    font-size: 12px;
    letter-spacing: 1px;
    color: var(--ink-white);
    opacity: 0.9;
  }
</style>
</head>
<body>
  <main class="canvas">
    <section class="card card-front" aria-label="Card front">
      <svg class="shapes" viewBox="0 0 520 297" preserveAspectRatio="none" aria-hidden="true">
        <rect width="520" height="297" fill="var(--card-white)"/>
        <circle cx="120" cy="40" r="250" fill="var(--teal-pale)" opacity="0.7"/>
        <circle cx="230" cy="-10" r="230" fill="var(--teal-light)" opacity="0.45"/>
        <circle cx="300" cy="210" r="215" fill="var(--teal)"/>
        <path d="M110 0 L520 110 L520 0 Z" fill="var(--ink-white)" opacity="0.12"/>
      </svg>
      <p class="signature-name">Lena Corvel</p>
    </section>

    <section class="card card-back" aria-label="Card back">
      <p class="web-address">itslenacorvel.com</p>
      <h1 class="name">Lena Corvel</h1>
      <p class="roles">Speaker | Digital Storyteller | Social Entrepreneur</p>
    </section>
  </main>
</body>
</html>
```